KLEM Athletics.com – Homepage Vision
KLEM is a community based youth sports program currently running basketball and soccer programs. We run recreational leagues, competitive club programs and run many camps, clinics and development programs in both sports.
My vision on the KLEM Home page was to design a clean page that will guide viewers quickly to the sport of interest.
At the top I was thinking of a KLEM Logo Bar. I want something that we can also customize for each of the sports to use in the future. So, 5 different logo bars.
1 – KLEM Athletics Logo Bar – Goes on the KLEMAthletics.com home page, which give general information about the club as a whole and leads folks to the sport they want to go.
2 – KLEM Basketball – Recreational. Same look as the homepage logo bar but only contains info regarding to recreational basketball.
3 – KLEM Basketball – Competitive. Same as above but only competitive basketball.
4 – KLEM Soccer – Recreational. Same as above but only recreational soccer.
5 – KLEM Soccer – Competitive. Same as above but only competitive soccer.
Maybe the logo bar on the home page can also be the main logo bar and also rotate the other 4 underneath the main logo bar. Logo are old, may need to be updated at some point.
The middle section, I was thinking of 4 boxes that when clicked on will take you to the appropriate website. The designs I used are just to show something. I took the picture off the web and they may be copyrighted so would probably need some type of original designs.
Recreational Basketball Website - http://klemathletics.example/basketball/index.html
Competitive Basketball Website - http://www.klemhornets.example/
Recreational Soccer Website - http://klemathletics.example/soccer/index.html
Competitive Soccer Website - http://www.prairiecrestsoccer.example/
Recreational basketball uses Willow Ridge Basketball (we own the trade name) or KLEM Basketball.
The competitive basketball club is known as KLEM Hornets.
Recreational soccer goes by Willow Ridge Soccer or Willow Ridge Soccer Club.
Competitive soccer goes by Prairie Crest Soccer or Willow Ridge Soccer Club.
Some logos we have used are attached. (KLEM Logos)
Then on the bottom of the page I was thinking of a menus bar that contains information general to the club (both basketball and soccer). When you click on any a pop up box will pop up with the information for each listed below.
About Us
Willow Ridge Athletic Club provides recreational leagues for both Basketball and Soccer with the focus placed on providing our youth with the rewarding opportunity of participating in youth sports. Our direction is to promote the recreational value of youth sports while emphasizing fun and respect for the sport.
Willow Ridge Athletic Club (KLEM) is based in the North Phoenix area with most of our players residing in the Stone Hollow School District.
Our Mission
Our mission at Willow Ridge Athletic Club is to promote and develop excellence in youth sports based on skill, sportsmanship, values, and player character. Our programs aim to provide an environment for natural player development that prepares them for life experiences, both on and off the field.
We focus on a uniform sports philosophy throughout the club that emphasizes growth through positive reinforcement resulting in players achieving his/her fullest potential. We do not look for the next victory to measure our success, but in the total learning experience for each player, realizing that the team is much stronger than an individual.
Contact Info
Willow Ridge Athletic Club
P.O. Box 7158
Stone Hollow, AZ 85990
Club Phone – 480-555-0173
Club Website – KLEMAthletics.com
Club Email – info@klemathletics.example
Basketball Email – KLEMBB@mailbox.example
Soccer Email – KLEMSoccer@inbox.example
Our Mission
The mission of KLEM shall be to promote good citizenship and health through community athletic activities for children and for educational purposes. Club focus is on player development, with emphasis on teamwork and sportsmanship with high standards for both parents and players. Respect, commitment and accountability are qualities we ask all our members to endorse both on and off the field.

```html
<!DOCTYPE html>
<html lang="en">
<head>
<meta charset="utf-8">
<title>KLEM Athletics – Home</title>
<link rel="stylesheet" href="https://fonts.googleapis.com/css2?family=Ubuntu:wght@400;500;700&display=swap">
<style>
  :root {
    --page-bg: #d9d9d6;
    --page-bg-light: #e6e6e3;
    --bar-green: #5d7a3f;
    --bar-green-dark: #4a6530;
    --sidebar-green: #4e6b32;
    --panel-green: #8ea874;
    --tile-green: #8cac6f;
    --white: #ffffff;
    --note-red: #e0231f;
    --photo-light: #d6d6d6;
    --photo-dark: #3a3a3a;
  }
  * { box-sizing: border-box; margin: 0; padding: 0; }
  html, body { width: 1200px; height: 675px; overflow: hidden; }
  body {
    position: relative;
    background: radial-gradient(ellipse at 30% 40%, var(--page-bg-light), var(--page-bg) 70%);
    font-family: "Ubuntu", sans-serif;
    color: var(--white);
  }
  .top-bar {
    position: absolute; left: 0; top: 0; width: 1200px; height: 56px;
    background: linear-gradient(var(--bar-green), var(--bar-green-dark));
    border-radius: 0 0 14px 14px;
    box-shadow: 0 3px 5px rgba(0,0,0,.35);
    z-index: 2;
  }
  .top-bar h1 {
    position: absolute; left: 418px; width: 539px; top: 2px;
    text-align: center; font-size: 48px; font-weight: 500; letter-spacing: 2px;
  }
  .sidebar {
    position: absolute; left: 296px; top: 56px; width: 106px; height: 619px;
    background: var(--sidebar-green);
  }
  .brand {
    position: absolute; left: 310px; top: 14px; width: 78px; z-index: 3;
    display: flex; flex-direction: column; align-items: center; gap: 4px;
  }
  .brand-mark {
    width: 62px; height: 62px; border-radius: 50%;
    border: 3px solid var(--white);
  }
  .brand-name { font-size: 14px; font-weight: 700; letter-spacing: 1px; }
  .sport-links { position: absolute; left: 231px; top: 81px; list-style: none; }
  .sport-tile {
    width: 61px; height: 62px; margin-bottom: 41px;
    background: var(--tile-green);
    border: 2px solid #e8efe0;
    box-shadow: 2px 2px 4px rgba(0,0,0,.3);
    position: relative;
  }
  .sport-tile svg { position: absolute; left: 6px; top: 6px; }
  .sport-tile .level {
    position: absolute; right: 4px; bottom: 2px; font-size: 9px; font-weight: 700;
  }
  .main-panel {
    position: absolute; left: 418px; top: 56px; width: 539px; height: 619px;
    background: var(--panel-green);
  }
  .intro-title {
    position: absolute; left: 418px; width: 510px; top: 101px;
    text-align: center; font-size: 29px; font-weight: 700; line-height: 38px;
  }
  .thumbs { position: absolute; left: 441px; top: 177px; }
  .thumb {
    width: 38px; height: 28px; margin-bottom: 6px;
    border: 1px solid #dfe6d6;
  }
  .thumb-1 { background: linear-gradient(135deg, #222, #8a8a8a 60%, #333); }
  .thumb-2 { background: linear-gradient(120deg, #bdbdbd, #f0f0f0 50%, #777); }
  .thumb-3 { background: linear-gradient(150deg, #8a8a8a, #eeeeee 55%, #a0a0a0); }
  .slide {
    position: absolute; left: 513px; top: 181px; width: 399px; height: 251px;
    background: linear-gradient(110deg, var(--photo-light) 0%, #bdbdbd 40%, #eaeaea 62%, var(--photo-dark) 78%, #151515 100%);
    box-shadow: 3px 3px 6px rgba(0,0,0,.4);
  }
  .slide-controls { position: absolute; left: 637px; top: 451px; display: flex; gap: 21px; }
  .slide-btn {
    width: 22px; height: 22px; border: 2px solid var(--white);
    display: flex; align-items: center; justify-content: center;
  }
  .tagline {
    position: absolute; left: 682px; top: 481px; width: 270px;
    font-size: 11px; font-weight: 700; line-height: 13.5px;
  }
  .pointer { position: absolute; left: 427px; top: 481px; }
  .design-note {
    position: absolute; left: 972px; top: 149px; width: 214px;
    color: var(--note-red); font-size: 14.4px; line-height: 18px; text-align: center;
  }
</style>
</head>
<body>
  <header class="top-bar"><h1>Welcome</h1></header>

  <aside class="sidebar"></aside>
  <div class="brand">
    <div class="brand-mark"></div>
    <span class="brand-name">KLEM</span>
  </div>

  <ul class="sport-links">
    <li class="sport-tile"><svg width="46" height="46" viewBox="0 0 46 46"><circle cx="23" cy="23" r="20" fill="none" stroke="#fff" stroke-width="3.5"/></svg><span class="level">R</span></li>
    <li class="sport-tile"><svg width="46" height="46" viewBox="0 0 46 46"><circle cx="23" cy="23" r="20" fill="none" stroke="#fff" stroke-width="3.5"/></svg><span class="level">C</span></li>
    <li class="sport-tile"><svg width="46" height="46" viewBox="0 0 46 46"><circle cx="23" cy="23" r="20" fill="none" stroke="#fff" stroke-width="3.5"/></svg><span class="level">R</span></li>
    <li class="sport-tile"><svg width="46" height="46" viewBox="0 0 46 46"><circle cx="23" cy="23" r="20" fill="none" stroke="#fff" stroke-width="3.5"/></svg><span class="level">C</span></li>
  </ul>

  <main class="main-panel"></main>
  <h2 class="intro-title">To Willow Ridge<br>Athletics Club</h2>

  <div class="thumbs">
    <div class="thumb thumb-1" role="img" aria-label="Slideshow thumbnail: flower photo"></div>
    <div class="thumb thumb-2" role="img" aria-label="Slideshow thumbnail: curved paper lines photo"></div>
    <div class="thumb thumb-3" role="img" aria-label="Slideshow thumbnail: white flower photo"></div>
  </div>
  <div class="slide" role="img" aria-label="Slideshow photo: black and white close-up of curved pleated lines"></div>

  <div class="slide-controls">
    <div class="slide-btn"><svg width="10" height="10" viewBox="0 0 10 10"><path d="M7 1 L3 5 L7 9" fill="none" stroke="#fff" stroke-width="1.8"/></svg></div>
    <div class="slide-btn"><svg width="10" height="10" viewBox="0 0 10 10"><path d="M3 1 L7 5 L3 9" fill="none" stroke="#fff" stroke-width="1.8"/></svg></div>
  </div>

  <svg class="pointer" width="232" height="82" viewBox="0 0 232 82">
    <polygon points="0,41 64,0 64,82" fill="#fff"/>
    <rect x="67" y="29" width="163" height="24" fill="#fff"/>
  </svg>

  <p class="tagline">Promoting good citizenship and health through community athletic activities for children<br>Please use our smart site bar to interact and find out everything you need to know, from timetables to try outs to how we where founded</p>

  <p class="design-note">A simple welcome page we only see for a brief moment as it guides us to the neet looking , double function menu bar. I have designed this light textured and sharp looking website with the simplicity you mentioned in mind. I have decided to do bit more then just design a home page the sleek green lay out is my master page and based on it all 4 of you`r websites can operate within it. All it would take is 3 to 4 working days to move all you content onto this layout. Sadly that’s all I can offer for you`r price if you where looking for a re-assembly and clean up of your current system you would have to up the budget a bit.The slide show bar will oviously be filed out with any pictures you desire to showcase.</p>
</body>
</html>
```